Makeup artist looking for business card design

- Business card to be memorable and recognisable

- I've attached photos of my logo (File 4), photos that I want to incorporate into the design (File 5,6 & 7) and an example of the design I like "Mirela Stott" (File 1)

- I've attached 3 photos of the designs I want to use, please use one of your choice

- Next to Instagram (File 2) and Facebook (File 3), please use their logo.

- No coloured background, either use the original background (grey) old white.

- Please include the following on the business card:
- Business name: LK Makeup Artistry
- My name: Rosalind Kerr
- Occupation: Makeup Artist
- Contact number: 0437 295 148
- Email: roskerr_makeup@mailvento.com
- Instagram (please use image): @lkmakeupartistry
- Facebook (please use image): www.facebook.com/LKMakeUpArtistry

Target Market(s)

Target woman for bridal makeup, occasion, fashion makeup and print.

Industry/Entity Type

Business

Requirements
Must have
• Logo provided and photo provided
Should not have
• Colourful background
Too cluttered
Shouldn't use old style font

```html
<!DOCTYPE html>
<html lang="en">
<head>
<meta charset="utf-8">
<title>LK Makeup Artistry – Business Card</title>
<link rel="stylesheet" href="https://fonts.googleapis.com/css2?family=Inter:wght@200;300&display=swap">
<style>
  :root {
    --card-grey: #d3cfce;
    --ink: #2a2627;
    --paper-white: #ffffff;
    --icon-tone: #a9a3a2;
  }
  * { margin: 0; padding: 0; box-sizing: border-box; }
  html, body {
    width: 668px;
    height: 1200px;
    overflow: hidden;
    background: var(--card-grey);
  }
  .card {
    position: relative;
    width: 668px;
    height: 1200px;
    background: var(--card-grey);
    font-family: "Inter", "Helvetica Neue", Arial, sans-serif;
    font-weight: 200;
    color: var(--ink);
  }
  .trim-line {
    position: absolute;
    top: 0;
    right: 0;
    width: 2px;
    height: 1200px;
  }
  .brand {
    position: absolute;
    top: 180px;
    left: 0;
    width: 100%;
    text-align: center;
    font-size: 34px;
    line-height: 44px;
    font-weight: 200;
    letter-spacing: 2px;
    color: var(--ink);
  }
  .identity {
    position: absolute;
    top: 448px;
    left: 0;
    width: 100%;
    text-align: center;
  }
  .identity__name {
    font-size: 62px;
    line-height: 76px;
    color: var(--paper-white);
    font-weight: 200;
    letter-spacing: 1px;
  }
  .identity__role {
    margin-top: 6px;
    font-size: 40px;
    line-height: 50px;
    letter-spacing: 3px;
  }
  .identity__phone {
    margin-top: 86px;
    font-size: 40px;
    line-height: 50px;
    letter-spacing: 4px;
  }
  .socials {
    position: absolute;
    top: 912px;
    left: 40px;
    list-style: none;
  }
  .socials__item {
    display: flex;
    align-items: center;
    height: 62px;
    margin-bottom: 13px;
  }
  .socials__marker {
    width: 58px;
    height: 58px;
    background: var(--icon-tone);
    flex: none;
  }
  .socials__label {
    margin-left: 16px;
    font-size: 36px;
  }
  .email {
    position: absolute;
    top: 1120px;
    left: 36px;
    font-size: 37px;
    line-height: 48px;
    letter-spacing: -0.5px;
    white-space: nowrap;
  }
  .email__prefix { color: var(--paper-white); }
</style>
</head>
<body>
  <main class="card">
    <svg class="trim-line" width="2" height="1200" aria-hidden="true">
      <line x1="1" y1="0" x2="1" y2="1200" stroke="#ffffff" stroke-width="1" stroke-dasharray="6 4"/>
    </svg>

    <header class="brand">LK Makeup Artistry</header>

    <section class="identity">
      <h1 class="identity__name">Rosalind Kerr</h1>
      <p class="identity__role">Makeup Artist</p>
      <p class="identity__phone">0437 295 148</p>
    </section>

    <ul class="socials">
      <li class="socials__item">
        <span class="socials__marker" aria-hidden="true"></span>
        <span class="socials__label">@lkmakeupartistry</span>
      </li>
      <li class="socials__item">
        <span class="socials__marker" aria-hidden="true"></span>
        <span class="socials__label">LK Makeup Artistry</span>
      </li>
    </ul>

    <p class="email"><span class="email__prefix">e:</span>roskerr_makeup@mailvento.com</p>
  </main>
</body>
</html>
```